Kestrel Drafts (Residential House Plans Company)

Want professional landing page to match our company theme. We provide custom house plans for primarily residential. We are structural engineers (not architects).

Prefer dark (black) theme but open to design options. Would like map of office location.

Address: 214 W Marlow Street, Oviedo, FL 32768
Phone: 407-582-6194
Email: office@kestreldrafts.example

Target Market(s)

Client who need custom house plans

Industry/Entity Type

Architecture, Structural Engineering

Coding

Coded - Design and coding required

Colors
0054AA
0677BA
7BADD7
CADEEF
E8F1F8

```html
<!DOCTYPE html>
<html lang="en">
<head>
<meta charset="utf-8">
<title>Kestrel Drafts – Custom House Plans</title>
<link href="https://fonts.googleapis.com/css2?family=Montserrat:wght@400;500;600;700;800&family=Oswald:wght@500;600&display=swap" rel="stylesheet">
<style>
:root{
  --bg:#05090f;
  --bg-panel:#071527;
  --card:#0b1a2e;
  --blue:#0677BA;
  --blue-bright:#1f7fd0;
  --deep:#0054AA;
  --light:#7BADD7;
  --pale:#CADEEF;
  --mist:#E8F1F8;
  --text:#c9d3de;
  --muted:#8d9aaa;
  --white:#ffffff;
}
*{margin:0;padding:0;box-sizing:border-box}
html,body{width:1200px;height:4216px;overflow:hidden}
body{background:var(--bg);font-family:"Montserrat",sans-serif;color:var(--text);position:relative}
.abs{position:absolute}
a{color:inherit;text-decoration:none}

/* hero */
.hero{left:0;top:0;width:1200px;height:599px;
  background:linear-gradient(180deg,#2c2a27 0%,#3c4a55 22%,#2f5a78 45%,#1d4f72 60%,#204a2a 80%,#162a1a 100%)}
.hero::after{content:"";position:absolute;inset:0;background:linear-gradient(180deg,rgba(0,0,0,.45),rgba(0,0,0,.05) 40%,rgba(0,0,0,.25))}
.brand{z-index:2;left:193px;top:34px;display:flex;align-items:center;gap:10px;color:var(--white);font-weight:800;font-size:30px;letter-spacing:.5px}
.brand-dot{width:18px;height:18px;background:var(--blue)}
.top-contact{z-index:2;top:36px;display:flex;gap:10px;align-items:center;color:var(--white);font-size:11.5px;line-height:19px}
.ring{width:28px;height:28px;border:1.5px solid rgba(255,255,255,.8);border-radius:50%;display:flex;align-items:center;justify-content:center}
.hero-title{z-index:2;left:0;width:1200px;top:284px;text-align:center;font-family:"Oswald",sans-serif;font-weight:600;font-size:45px;line-height:48px;color:var(--white);text-transform:uppercase}
.btn{display:flex;align-items:center;justify-content:center;font-size:12px;font-weight:600;letter-spacing:.5px;text-transform:uppercase}
.btn-white{z-index:2;left:532px;top:390px;width:119px;height:41px;background:var(--white);color:#111;border-radius:2px}
.btn-blue{background:var(--blue);color:var(--white);border-radius:2px}

/* headings */
.h2{font-weight:800;font-size:39px;letter-spacing:1px;text-transform:uppercase;line-height:1.15}
.h2 .outline{color:transparent;-webkit-text-stroke:1.2px #7d8894;font-weight:500}
.h2 .solid{color:var(--blue-bright)}
.center{left:0;width:1200px;text-align:center}
.lead{font-size:15.5px;line-height:27px;color:#d5dce4}
.body-copy{font-size:15px;line-height:29px;color:#c3ccd6}
.small-copy{font-size:12px;line-height:20.5px;color:#b3bdc8}

.link{display:flex;align-items:center;gap:14px;color:var(--blue-bright);font-size:12px;letter-spacing:1.2px;text-transform:uppercase;text-decoration:underline}
.link-box{width:41px;height:41px;background:#0f2947;display:flex;align-items:center;justify-content:center}
.link-box.sm{width:26px;height:26px}

/* about */
.about-media{left:0;top:622px;width:557px;height:524px;background:linear-gradient(135deg,#1b2633 0%,#2a3848 45%,#0b1320 100%)}
.about-media-name{left:150px;top:800px;color:var(--white);font-weight:800;font-size:52px}

/* services */
.service-title{font-size:15.5px;font-weight:600;color:var(--white)}
.drawing-card{background:var(--white);border-radius:6px;box-shadow:7px 7px 0 var(--blue)}
.drawing-fill{position:absolute;inset:14px;background:linear-gradient(180deg,#f4f6f8,#e4e8ec);border-radius:3px}

/* slider */
.arrow{width:41px;height:41px;display:flex;align-items:center;justify-content:center;border-radius:2px}
.arrow.dark{background:#102640}
.arrow.blue{background:var(--blue)}
.slide{left:254px;top:2279px;width:692px;height:386px;background:var(--white);border-radius:6px}

/* testimonials */
.quote-card{width:400px;height:163px;background:var(--card);padding:38px 34px 0 34px;font-size:11.8px;line-height:20px;color:#c3ccd6}
.quote-card::after{content:"";position:absolute;left:46px;bottom:-18px;border-left:18px solid transparent;border-right:0;border-top:18px solid var(--card)}
.quote-mark{position:absolute;left:34px;top:-10px}
.avatar{width:48px;height:48px;background:linear-gradient(135deg,#5d6670,#2c3239)}
.person-name{font-size:13.5px;font-weight:600;color:var(--white)}
.person-place{font-size:10.5px;color:var(--muted);margin-top:6px}

/* contact */
.contact-band{left:0;top:3304px;width:1200px;height:510px;background:linear-gradient(180deg,#081a30,#06152a)}
.info-row{left:142px;display:flex;gap:20px}
.info-icon{width:38px;height:38px;background:#0f2947;display:flex;align-items:center;justify-content:center;flex:none}
.info-label{font-size:14px;font-weight:700;color:var(--white)}
.info-value{font-size:12.5px;color:#c3ccd6;margin-top:6px}
.divider{left:142px;width:340px;height:1px;background:#1a2d44}
.field{background:#0a1d33;font-size:12px;color:#8b98a8;padding:0 22px;display:flex;align-items:center}

/* newsletter */
.newsletter{left:142px;top:3876px;width:917px;height:199px;border:4px solid #2a2e33}
.check{width:22px;height:22px;background:#0f2947}

/* footer */
.footer-line{left:142px;top:4133px;width:917px;height:1px;background:#1f2731}
.social{width:33px;height:33px;background:#0f2947}
</style>
</head>
<body>

<!-- Hero -->
<header class="abs hero" role="img" aria-label="Aerial photograph of a lakeside city skyline at dusk"></header>
<div class="abs brand"><span>Kestrel Drafts</span></div>
<div class="abs top-contact" style="left:717px">
  <div class="ring"><svg width="14" height="14" viewBox="0 0 24 24" fill="none" stroke="#fff" stroke-width="2"><path d="M5 3h4l2 5-3 2a11 11 0 0 0 6 6l2-3 5 2v4a2 2 0 0 1-2 2A18 18 0 0 1 3 5a2 2 0 0 1 2-2z"/></svg></div>
  <div>Phone<br>407-582-6194</div>
</div>
<div class="abs top-contact" style="left:855px">
  <div class="ring"><svg width="14" height="14" viewBox="0 0 24 24" fill="none" stroke="#fff" stroke-width="2"><path d="M12 22s7-7 7-12a7 7 0 0 0-14 0c0 5 7 12 7 12z"/><circle cx="12" cy="10" r="2.5"/></svg></div>
  <div>214 W Marlow Street<br>Oviedo, FL 32768</div>
</div>
<h1 class="abs hero-title">We provide custom house plans for<br>residential customers</h1>
<a class="abs btn btn-white" href="#contact">Contact Us</a>

<!-- About -->
<div class="abs about-media" role="img" aria-label="Modern building photograph in cool blue tones"></div>
<div class="abs about-media-name">Kestrel Drafts</div>
<h2 class="abs h2" style="left:578px;top:683px"><span class="outline">About</span> <span class="solid">Us</span></h2>
<p class="abs body-copy" style="left:578px;top:747px;width:470px">Lorem ipsum dolor sit amet, consectetuer adipiscing elit, sed diam nonummy nibh euismod tincidunt ut laoreet dolore magna aliquam erat volutpat. Ut wisi enim ad minim veniam, quis nostrud exerci tation ullamcorper suscipit lobortis nisl ut aliquip ex ea commodo consequat. Duis autem vel eum iriure dolor in hendrerit in vulputate velit esse molestie consequat, vel illum dolore eu feugiat nulla facilisisea commodo consequat. Duis autem vel eum iriure dolor in hendrerit ...</p>
<a class="abs link" style="left:578px;top:1007px" href="#"><span class="link-box"><svg width="14" height="14" viewBox="0 0 24 24" fill="none" stroke="#1f7fd0" stroke-width="2"><path d="M6 6l12 12M18 8v10H8"/></svg></span>Read More</a>

<!-- Services -->
<h2 class="abs h2 center" style="top:1124px"><span class="outline">Our</span> <span class="solid">Services</span></h2>
<p class="abs lead center" style="top:1184px">Lorem ipsum dolor sit amet, consectetuer adipiscing elit, sed diam nonummy<br>nibh euismod tincidunt ut laoreet dolore magna aliquam erat volutpat.</p>

<svg class="abs" style="left:148px;top:1320px" width="70" height="66" viewBox="0 0 70 66" fill="none" stroke="#1f7fd0" stroke-width="2.5"><path d="M4 32L35 6l31 26M12 26v34h46V26"/><rect x="22" y="34" width="10" height="10"/><rect x="38" y="34" width="10" height="10"/><path d="M30 60V50h10v10"/></svg>
<h3 class="abs service-title" style="left:142px;top:1409px">Custom House Plans</h3>
<p class="abs small-copy" style="left:142px;top:1437px;width:390px">Lorem ipsum dolor sit amet, consectetuer adipiscing elit, sed diam nonummy nibh euismod tincidunt ut laoreet dolore magna aliquam erat volutpat. Ut wisi enim ad minim veniam, quis nostrud exerci tation ullamcorper suscipit lobortis nisl u...</p>
<a class="abs link" style="left:142px;top:1531px;font-size:10.5px" href="#"><span class="link-box sm"><svg width="10" height="10" viewBox="0 0 24 24" fill="none" stroke="#1f7fd0" stroke-width="2.5"><path d="M6 6l12 12M18 8v10H8"/></svg></span>All Details</a>
<div class="abs drawing-card" style="left:593px;top:1278px;width:459px;height:316px"><div class="drawing-fill" role="img" aria-label="First and second floor plan drawings"></div></div>

<div class="abs drawing-card" style="left:142px;top:1667px;width:464px;height:316px"><div class="drawing-fill" role="img" aria-label="Structural framing detail drawings"></div></div>
<svg class="abs" style="left:670px;top:1704px" width="52" height="72" viewBox="0 0 52 72" fill="none" stroke="#1f7fd0" stroke-width="2.5"><path d="M8 24a18 18 0 0 1 36 0zM4 26h44M26 6v10"/><path d="M6 70V56a20 12 0 0 1 40 0v14M18 50v20M34 50v20"/></svg>
<h3 class="abs service-title" style="left:674px;top:1800px">Civil &amp; Structural Engineering</h3>
<p class="abs small-copy" style="left:674px;top:1829px;width:390px">Lorem ipsum dolor sit amet, consectetuer adipiscing elit, sed diam nonummy nibh euismod tincidunt ut laoreet dolore magna aliquam erat volutpat. Ut wisi enim ad minim veniam, quis nostrud exerci tation ullamcorper suscipit lobortis nisl u...</p>
<a class="abs link" style="left:682px;top:1924px;font-size:10.5px" href="#"><span class="link-box sm"><svg width="10" height="10" viewBox="0 0 24 24" fill="none" stroke="#1f7fd0" stroke-width="2.5"><path d="M6 6l12 12M18 8v10H8"/></svg></span>All Details</a>

<a class="abs btn btn-blue" style="left:540px;top:2035px;width:120px;height:41px" href="#contact">Contact Us</a>

<!-- House plan slider -->
<h2 class="abs h2 center" style="top:2152px"><span class="outline">House</span> <span class="solid">Plan</span></h2>
<p class="abs lead center" style="top:2211px">Lorem ipsum dolor sit amet, consectetuer adipiscing elit, sed diam nonummy.</p>
<div class="abs arrow dark" style="left:142px;top:2452px"><svg width="16" height="16" viewBox="0 0 24 24" fill="none" stroke="#fff" stroke-width="2"><path d="M20 12H4M10 6l-6 6 6 6"/></svg></div>
<div class="abs slide"><div class="drawing-fill" style="inset:18px 40px" role="img" aria-label="House floor plan drawing"></div></div>
<div class="abs arrow blue" style="left:1017px;top:2452px"><svg width="16" height="16" viewBox="0 0 24 24" fill="none" stroke="#fff" stroke-width="2"><path d="M4 12h16M14 6l6 6-6 6"/></svg></div>
<a class="abs btn btn-blue" style="left:504px;top:2711px;width:192px;height:41px" href="#">Browse House Plans</a>

<!-- Testimonials -->
<h2 class="abs h2" style="left:142px;top:2826px;line-height:50px"><span class="outline">What our</span><br><span class="solid">Customers say</span></h2>
<div class="abs arrow dark" style="left:958px;top:2873px"><svg width="16" height="16" viewBox="0 0 24 24" fill="none" stroke="#fff" stroke-width="2"><path d="M20 12H4M10 6l-6 6 6 6"/></svg></div>
<div class="abs arrow blue" style="left:1017px;top:2873px"><svg width="16" height="16" viewBox="0 0 24 24" fill="none" stroke="#fff" stroke-width="2"><path d="M4 12h16M14 6l6 6-6 6"/></svg></div>

<div class="abs quote-card" style="left:170px;top:2956px">
  <svg class="quote-mark" width="32" height="24" viewBox="0 0 32 24" fill="#1f7fd0"><path d="M0 24V10L6 0h7L9 10h5v14zM18 24V10l6-10h7l-4 10h5v14z"/></svg>
  Lorem ipsum dolor sit amet, consectetuer adipiscing elit, sed diam nonummy nibh euismod tincidunt ut laoreet dolore magna aliquam erat volutpat. Ut wisi enim ad minim veniam, quis nostrud exerci tation ullamcorper suscipit lobortis nisl u...
</div>
<div class="abs" style="left:170px;top:3156px;display:flex;gap:18px;align-items:center">
  <div class="avatar" role="img" aria-label="Customer portrait photo"></div>
  <div><div class="person-name">Dana from Reading</div><div class="person-place">123, Lorem ipsum sit, USA</div></div>
</div>

<div class="abs quote-card" style="left:629px;top:2956px">
  <svg class="quote-mark" width="32" height="24" viewBox="0 0 32 24" fill="#1f7fd0"><path d="M0 24V10L6 0h7L9 10h5v14zM18 24V10l6-10h7l-4 10h5v14z"/></svg>
  Lorem ipsum dolor sit amet, consectetuer adipiscing elit, sed diam nonummy nibh euismod tincidunt ut laoreet dolore magna aliquam erat volutpat. Ut wisi enim ad minim veniam, quis nostrud exerci tation ullamcorper suscipit lobortis nisl u...
</div>
<div class="abs" style="left:629px;top:3156px;display:flex;gap:18px;align-items:center">
  <div class="avatar" style="background:linear-gradient(135deg,#c9a57a,#6d5440)" role="img" aria-label="Customer portrait photo"></div>
  <div><div class="person-name">Omar from Basingstoke</div><div class="person-place">123, Lorem ipsum sit, USA</div></div>
</div>

<!-- Contact -->
<section class="abs contact-band" id="contact"></section>
<h2 class="abs h2" style="left:142px;top:3372px"><span class="outline">Contact</span> <span class="solid">Info</span></h2>
<div class="abs info-row" style="top:3452px">
  <div class="info-icon"><svg width="16" height="16" viewBox="0 0 24 24" fill="#1f7fd0"><path d="M12 22s7-7 7-12a7 7 0 0 0-14 0c0 5 7 12 7 12z"/><circle cx="12" cy="10" r="2.5" fill="#0f2947"/></svg></div>
  <div><div class="info-label">Address :</div><div class="info-value">214 W Marlow Street, Oviedo, FL 32768</div></div>
</div>
<div class="abs divider" style="top:3516px"></div>
<div class="abs info-row" style="top:3542px">
  <div class="info-icon"><svg width="16" height="16" viewBox="0 0 24 24" fill="#1f7fd0"><path d="M5 3h4l2 5-3 2a11 11 0 0 0 6 6l2-3 5 2v4a2 2 0 0 1-2 2A18 18 0 0 1 3 5a2 2 0 0 1 2-2z"/></svg></div>
  <div><div class="info-label">Call Us :</div><div class="info-value">407-582-6194</div></div>
</div>
<div class="abs divider" style="top:3604px"></div>
<div class="abs info-row" style="top:3630px">
  <div class="info-icon"><svg width="16" height="16" viewBox="0 0 24 24" fill="none" stroke="#1f7fd0" stroke-width="2"><rect x="3" y="5" width="18" height="14"/><path d="M3 6l9 7 9-7"/></svg></div>
  <div><div class="info-label">Email – ID :</div><div class="info-value">office@kestreldrafts.example</div></div>
</div>

<h2 class="abs h2" style="left:548px;top:3372px"><span class="outline">Contact</span> <span class="solid">Form</span></h2>
<div class="abs field" style="left:548px;top:3447px;width:246px;height:45px">First Name*</div>
<div class="abs field" style="left:808px;top:3447px;width:251px;height:45px">Phone No*</div>
<div class="abs field" style="left:548px;top:3508px;width:511px;height:45px">Email Address*</div>
<div class="abs field" style="left:548px;top:3569px;width:511px;height:90px;align-items:flex-start;padding-top:16px">Your Message..</div>
<a class="abs link" style="left:548px;top:3691px" href="#"><span class="link-box" style="background:var(--blue)"><svg width="14" height="14" viewBox="0 0 24 24" fill="none" stroke="#fff" stroke-width="2"><path d="M6 6l12 12M18 8v10H8"/></svg></span>Send</a>

<!-- Newsletter -->
<div class="abs newsletter"></div>
<h2 class="abs h2" style="left:182px;top:3928px;font-size:34px;line-height:46px"><span class="outline">Subscribe to our</span><br><span class="solid">Newsletter</span></h2>
<div class="abs field" style="left:583px;top:3935px;width:306px;height:46px;color:#b7c2ce">Your Email Address</div>
<a class="abs btn btn-blue" style="left:889px;top:3935px;width:137px;height:46px;font-size:11.5px" href="#">Subscribe</a>
<div class="abs check" style="left:583px;top:3997px"></div>
<div class="abs" style="left:616px;top:4001px;font-size:11px;color:#b7c2ce">I Agree With Terms &amp; Conditions</div>

<!-- Footer -->
<div class="abs footer-line"></div>
<div class="abs" style="left:142px;top:4174px;font-size:11.5px;color:#c3ccd6">© 2023 Kestrel Drafts. All Rights Reserved.</div>
<div class="abs" style="left:897px;top:4165px;display:flex;gap:9px">
  <div class="social" aria-label="Social profile"></div>
  <div class="social" aria-label="Social profile"></div>
  <div class="social" aria-label="Social profile"></div>
  <div class="social" aria-label="Social profile"></div>
</div>

</body>
</html>
```